Diesel injection diagnostics and repairs

I am after a business card design for my business.
The business; repairs diesel fuel systems on 4wds, trucks, earthmoving equipment,can do mobile repairs and diagnostics
The business design can basic but effective, I guess some colours such as green and black or even blue......
The end result should reflect the business name and logo and what the business can do

Industry/Entity Type

Business

Contact Information for Business Card

TB Diesel Injection PTY LTD
tb_diesel@mailbox-example.net
Nathan Bowers
0491570156

```html
<!DOCTYPE html>
<html lang="en">
<head>
<meta charset="UTF-8">
<title>TB Diesel Injection PTY LTD – Business Card</title>
<link rel="stylesheet" href="https://fonts.googleapis.com/css2?family=Open+Sans:wght@400;600;700&display=swap">
<style>
  :root {
    --backdrop: #f4f4f4;
    --kraft: #c9bfae;
    --kraft-edge: #b9ae9b;
    --ink: #262522;
    --ink-soft: #3a3935;
    --rule: #55534f;
  }
  * { box-sizing: border-box; margin: 0; padding: 0; }
  html, body {
    width: 1200px;
    height: 918px;
    overflow: hidden;
    background: var(--backdrop);
    font-family: "Open Sans", Arial, sans-serif;
    color: var(--ink);
  }
  .canvas {
    position: relative;
    width: 1200px;
    height: 918px;
  }
  .card {
    position: absolute;
    background: var(--kraft);
    border: 1px solid var(--kraft-edge);
    box-shadow: 0 14px 30px rgba(0,0,0,0.12);
  }

  /* Front of card */
  .card-front {
    left: 60px;
    top: 304px;
    width: 540px;
    height: 310px;
  }
  .company-block {
    position: absolute;
    right: 28px;
    top: 26px;
    text-align: right;
  }
  .company-name {
    font-size: 23px;
    font-weight: 700;
    line-height: 1.15;
  }
  .company-tagline {
    font-size: 13px;
    font-weight: 700;
    line-height: 1.3;
    margin-top: 4px;
    color: var(--ink-soft);
  }
  .brand-mark {
    position: absolute;
    left: 34px;
    top: 118px;
    display: flex;
    align-items: center;
    gap: 10px;
  }
  .brand-mark-square {
    width: 18px;
    height: 18px;
    background: var(--ink);
  }
  .brand-mark-name {
    font-size: 20px;
    font-weight: 700;
    color: var(--ink);
  }
  .contact-block {
    position: absolute;
    right: 28px;
    top: 150px;
    text-align: right;
    font-size: 14px;
    line-height: 1.55;
    color: var(--ink-soft);
    letter-spacing: 0.3px;
  }
  .person-name {
    position: absolute;
    left: 34px;
    bottom: 30px;
    font-size: 25px;
    font-weight: 700;
  }

  /* Back of card */
  .card-back {
    left: 770px;
    top: 189px;
    width: 310px;
    height: 540px;
  }
  .card-back svg {
    position: absolute;
    inset: 0;
  }
  .back-company {
    font-family: "Open Sans", Arial, sans-serif;
    font-size: 25px;
    font-weight: 700;
    fill: var(--ink);
  }
  .back-web {
    font-family: "Open Sans", Arial, sans-serif;
    font-size: 13px;
    font-weight: 400;
    fill: var(--ink-soft);
    letter-spacing: 0.3px;
  }
  .back-rule {
    stroke: var(--rule);
    stroke-width: 3;
  }
</style>
</head>
<body>
<main class="canvas">

  <section class="card card-front" aria-label="Business card front">
    <div class="company-block">
      <p class="company-name">TB Diesel Injection PTY LTD</p>
      <p class="company-tagline">repairs diesel fuel systems on 4wds<br>mobile repairs and diagnostics</p>
    </div>

    <div class="brand-mark">
      <span class="brand-mark-square"></span>
      <span class="brand-mark-name">TB Diesel</span>
    </div>

    <div class="contact-block">
      <p class="contact-email">tb_diesel@mailbox-example.net</p>
      <p class="contact-phone">0491570156</p>
    </div>

    <p class="person-name">Nathan Bowers</p>
  </section>

  <section class="card card-back" aria-label="Business card back">
    <svg width="310" height="540" viewBox="0 0 310 540" xmlns="http://www.w3.org/2000/svg">
      <line class="back-rule" x1="70" y1="92" x2="150" y2="92"/>
      <line class="back-rule" x1="130" y1="70" x2="130" y2="470"/>
      <text class="back-company" transform="translate(140 98) rotate(90)">TB Diesel Injection PTY LTD</text>
      <text class="back-web" transform="translate(70 160) rotate(90)">www.tbdiesel-example.net</text>
    </svg>
  </section>

</main>
</body>
</html>
```